Author and Publisher

Cover for a book on the process of publishing a book from the presentation to the publisher until the selling in bookstores :
A behind-the-scenes journey through the world of book publishing, from manuscript to bookstore. The book explores the relationship between authors and publishers, manuscript selection, contracts, editing, proofreading, book design, printing, distribution, bookstores and online sales. It reveals the many people, decisions and processes involved in turning a text into a physical book and bringing it to readers. The illustration should evoke publishing as a lively, contemporary ecosystem, combining creativity, craftsmanship, business and the enduring appeal of books.
FORMAT : 14 x 20,5 cm
AUTHOR : Luc Varennes
TITLE : Le scribe et la presse
PUBLISHER : Editions Trovel (at the bottom of the page)
Target Market(s)
General public, mainly news authors of books
Look and feel
Each slider illustrates characteristics of the customer's brand and the style your logo design should communicate.

```html
<!DOCTYPE html>
<html lang="fr">
<head>
<meta charset="utf-8">
<title>Le scribe et la presse — Luc Varennes</title>
<link rel="stylesheet" href="https://fonts.googleapis.com/css2?family=Abril+Fatface&family=Playfair+Display:ital,wght@1,900&family=Poppins:wght@500;700&display=swap">
<style>
  :root {
    --backdrop: #bf9094;
    --paper: #ddd5c6;
    --paper-edge: #d0c6b5;
    --ink: #1f1c1a;
    --title-white: #fbf8f2;
    --desk-shadow: #2c302b;
    --desk-wood: #b58a55;
    --desk-lamp: #d9b77a;
    --sweater-grey: #6f6e6a;
    --press-dark: #262e30;
    --press-steel: #5d6a6d;
    --press-light: #c9cfd0;
    --shelf-dark: #2e2622;
    --shelf-warm: #b8743e;
    --shelf-spines: #c9a25a;
    --shelf-cool: #6f7f86;
  }
  * { margin: 0; padding: 0; box-sizing: border-box; }
  html, body { width: 1200px; height: 795px; overflow: hidden; background: var(--backdrop); }
  .canvas { width: 1200px; height: 795px; display: flex; align-items: center; justify-content: center; }

  .cover {
    position: relative; width: 509px; height: 745px; overflow: hidden;
    background: radial-gradient(ellipse at 50% 40%, var(--paper) 55%, var(--paper-edge) 100%);
  }

  .author {
    position: absolute; top: 27px; left: 0; right: 0; text-align: center;
    font-family: "Poppins", sans-serif; font-weight: 700; font-size: 18px;
    letter-spacing: 0.5em; padding-left: 0.5em; color: var(--ink);
  }

  .photo {
    position: absolute;
    -webkit-mask-image: radial-gradient(ellipse closest-side, #000 72%, transparent 100%);
            mask-image: radial-gradient(ellipse closest-side, #000 72%, transparent 100%);
  }
  .photo-writer {
    left: 140px; top: 72px; width: 350px; height: 260px;
    background:
      linear-gradient(200deg, var(--desk-shadow) 0%, var(--desk-shadow) 28%, rgba(44,48,43,0) 50%),
      linear-gradient(90deg, var(--desk-lamp) 0%, var(--desk-wood) 45%, var(--sweater-grey) 72%, var(--desk-shadow) 100%);
  }
  .photo-printer {
    left: -40px; top: 288px; width: 290px; height: 258px;
    background:
      linear-gradient(160deg, var(--press-dark) 0%, var(--press-steel) 45%, var(--press-light) 78%, var(--press-steel) 100%);
  }
  .photo-reader {
    left: 170px; top: 470px; width: 320px; height: 262px;
    background:
      linear-gradient(90deg, var(--shelf-cool) 0%, var(--shelf-spines) 25%, var(--shelf-warm) 48%, var(--shelf-dark) 68%, var(--shelf-dark) 100%);
  }

  .title { font-weight: normal; }
  .title-line {
    position: absolute; font-family: "Abril Fatface", serif; color: var(--title-white);
    line-height: 1; white-space: nowrap; text-shadow: 0 2px 5px rgba(0,0,0,0.3);
  }
  .title-first { left: 20px; top: 96px; font-size: 74px; }
  .title-join {
    position: absolute; left: 58px; top: 170px;
    font-family: "Playfair Display", serif; font-style: italic; font-weight: 900;
    font-size: 50px; line-height: 1; color: var(--title-white);
    text-shadow: 0 2px 5px rgba(0,0,0,0.3);
  }
  .title-second { left: 182px; top: 344px; font-size: 74px; }

  .publisher {
    position: absolute; left: 22px; top: 612px;
    font-family: "Poppins", sans-serif; font-weight: 500; font-size: 19px; color: var(--ink);
  }
</style>
</head>
<body>
<main class="canvas">
  <article class="cover">
    <p class="author">LUC VARENNES</p>

    <div class="photo photo-writer" role="img" aria-label="Photo d'un auteur, vu de dos, tapant son manuscrit sur un ordinateur portable à un bureau en bois"></div>
    <div class="photo photo-printer" role="img" aria-label="Photo d'un imprimeur en salopette vérifiant un nuancier de couleurs dans un atelier d'impression"></div>
    <div class="photo photo-reader" role="img" aria-label="Photo d'un lecteur feuilletant un livre devant les rayonnages colorés d'une librairie"></div>

    <h1 class="title">
      <span class="title-line title-first">Le scribe</span>
      <span class="title-join">et</span>
      <span class="title-line title-second">la presse</span>
    </h1>

    <p class="publisher">Editions Trovel</p>
  </article>
</main>
</body>
</html>
```